Commercial and Residential Paint Contractor needs website

We need a website for our residential painting, multi-family painting and commercial painting company. We paint interior and exterior of houses, apartments and commercial buildings. I would like an about us page, residential page, multi family page, commercial page and contact us. Need keywords added to website for seo opitimazation. I like this website https://www.glossfieldworks.com/

Target Market(s)

General Contractors and commercial property managers

Coding

Coded - Design and coding required

Number of Pages Required

5+ page

Font styles to use
Sans Serif

Requirements
Must have
• I need SEO keywords on pages

```html
<!DOCTYPE html>
<html lang="en">
<head>
<meta charset="utf-8">
<title>Hartwell Painting | Residential, Multi Family and Commercial Painting</title>
<link rel="stylesheet" href="https://fonts.googleapis.com/css2?family=Montserrat:wght@400;500;600;700&family=Roboto:wght@500;700&display=swap">
<style>
:root{
  --navy:#1e4395;
  --red:#d9232e;
  --footer:#28308c;
  --ink:#333a45;
  --soft:#eef1f5;
  --field:#e9ecef;
  --white:#ffffff;
  --sky:#a9dcf0;
}
*{box-sizing:border-box;margin:0;padding:0}
html,body{width:1200px;height:5272px;overflow:hidden}
body{position:relative;font-family:"Montserrat",sans-serif;color:var(--ink);background:var(--white)}
.abs{position:absolute}
.photo{position:absolute;display:block}
h1,h2,h3{font-family:"Roboto",sans-serif;font-weight:700}
.btn{position:absolute;background:var(--red);color:var(--white);font-family:"Roboto",sans-serif;font-weight:500;font-size:24px;display:flex;align-items:center;justify-content:center;text-decoration:none}

/* hero */
.hero{position:absolute;left:0;top:0;width:1200px;height:693px;background:linear-gradient(90deg,#f2f3f2 0%,#f6f7f6 55%,var(--sky) 68%,#c2e7f5 100%)}
.hero-photo{left:0;top:210px;width:560px;height:483px;background:linear-gradient(160deg,#e9ded4 0%,#2e63c4 55%,#1f4da8 100%)}
.site-header{position:absolute;left:98px;top:55px;width:1004px;height:120px;background:var(--white);box-shadow:0 4px 14px rgba(0,0,0,.15)}
.brand{position:absolute;left:26px;top:28px;display:flex;align-items:center;gap:12px;font-family:"Roboto",sans-serif;font-weight:700;font-size:44px;color:var(--navy);letter-spacing:1px}
.brand-dot{width:22px;height:22px;background:var(--red)}
.nav{position:absolute;left:360px;top:44px;display:flex;gap:0;font-family:"Montserrat",sans-serif;font-weight:600;font-size:23px;color:#222}
.nav a{color:inherit;text-decoration:none;padding:0 26px;border-right:2px solid #222;line-height:24px;position:relative}
.nav a:first-child{padding-left:0}
.nav a:last-child{border-right:0;padding-right:0}
.nav a.active::after{content:"";position:absolute;left:0;right:24px;bottom:-14px;height:7px;border-radius:4px;background:var(--red)}
.hero-copy{position:absolute;left:760px;top:240px;width:380px;text-align:center;font-family:"Roboto",sans-serif;font-weight:500;font-size:62px;line-height:71px;color:#111}
.hero-copy .accent{color:var(--navy)}
.hero-btn{left:848px;top:558px;width:200px;height:48px}

/* section titles */
.title{position:absolute;left:0;width:1200px;text-align:center;font-size:52px;color:var(--navy);letter-spacing:1px}
.rule{position:absolute;left:470px;width:260px;height:20px}
.intro{position:absolute;left:110px;width:980px;text-align:center;font-weight:600;font-size:20.5px;line-height:25.5px;color:#333}

/* phone band */
.band-line{position:absolute;left:0;top:1096px;width:1200px;border-top:2px dashed var(--navy)}
.phone{position:absolute;left:462px;top:1060px;width:274px;height:70px;background:var(--red);color:var(--white);font-family:"Roboto",sans-serif;font-weight:500;font-size:33px;display:flex;align-items:center;justify-content:center;letter-spacing:1px}

/* services */
.services{position:absolute;left:0;top:1098px;width:1200px;height:1860px;background:var(--soft)}
.panel{position:absolute;background:var(--white)}
.service-title{position:absolute;font-size:35px;color:var(--navy)}
.service-text{position:absolute;font-size:20.5px;line-height:25.5px;color:#333;width:380px}
.service-btn{width:142px;height:42px;font-size:22px}
.brush{position:absolute}

/* gallery */
.gallery-tile{position:absolute;width:394px;height:278px}

/* quote form */
.quote-bg{position:absolute;left:536px;top:4294px;width:664px;height:588px;background:var(--soft)}
.quote-title{position:absolute;left:598px;top:4340px;font-size:50px;line-height:64px;color:var(--navy)}
.field{position:absolute;left:598px;width:549px;background:var(--field);font-size:20px;color:#666;padding:16px 16px}

/* footer */
.footer{position:absolute;left:0;top:4884px;width:1200px;height:388px;background:var(--footer);color:var(--white)}
.footer-brand{position:absolute;left:0;top:88px;width:1200px;display:flex;justify-content:center;align-items:center;gap:14px;font-family:"Roboto",sans-serif;font-weight:700;font-size:56px;letter-spacing:1px}
.footer-brand .brand-dot{background:var(--red)}
.footer h3{position:absolute;font-family:"Montserrat",sans-serif;font-weight:600;font-size:25px}
.contact-row{position:absolute;display:flex;align-items:center;gap:12px;font-weight:600;font-size:19px}
.footer-note{position:absolute;left:390px;top:218px;width:420px;text-align:center;font-weight:600;font-size:13.5px;line-height:16px}
.license{position:absolute;left:878px;font-weight:600;font-size:19px}
</style>
</head>
<body>

<!-- hero -->
<section class="hero">
  <div class="photo hero-photo" role="img" aria-label="Painter in a white cap rolling white paint over a blue wall"></div>
  <header class="site-header">
    <div class="brand"><span class="brand-dot"></span>HARTWELL</div>
    <nav class="nav">
      <a class="active" href="#">Home</a>
      <a href="#">Services</a>
      <a href="#">Gallery</a>
      <a href="#">Blog</a>
      <a href="#">Contact</a>
    </nav>
  </header>
  <h1 class="hero-copy">Now<br><span class="accent">Durability</span><br>is also<br><span class="accent">Affordable</span></h1>
  <a class="btn hero-btn" href="#">Connect Now</a>
</section>

<!-- about -->
<h2 class="title" style="top:748px">ABOUT US</h2>
<svg class="rule" style="top:812px" viewBox="0 0 260 20"><line x1="0" y1="9" x2="95" y2="9" stroke="#d9232e" stroke-width="2"/><line x1="165" y1="9" x2="260" y2="9" stroke="#d9232e" stroke-width="2"/><path d="M118 3h24v7h-24z M128 10h4v10h-4z" fill="none" stroke="#d9232e" stroke-width="2"/></svg>
<p class="intro" style="top:860px">We are family owned and operated with over 10 years' experience. We pride our self in performing to the highest degree of workmanship standards. Hartwell Painting is your best choice for commercial, residential and multi-family painting in the DFW/Forth Worth area. Our experienced estimators willnmeet with you and customize a proposal to meet your needs. They will stay with you from the beginning of the project to the end, making sure you are 100% satisfied.</p>

<div class="band-line"></div>

<!-- services -->
<section class="services">
  <h2 class="title" style="top:78px">SERVICES</h2>
  <svg class="rule" style="top:138px" viewBox="0 0 260 20"><line x1="0" y1="9" x2="95" y2="9" stroke="#d9232e" stroke-width="2"/><line x1="165" y1="9" x2="260" y2="9" stroke="#d9232e" stroke-width="2"/><path d="M118 3h24v7h-24z M128 10h4v10h-4z" fill="none" stroke="#d9232e" stroke-width="2"/></svg>
  <p class="intro" style="top:168px;font-weight:500">Lorem ipsum, or lipsum as it is sometimes known, is dummy text</p>

  <!-- residential -->
  <div class="panel" style="left:0;top:392px;width:478px;height:330px"></div>
  <div class="brush" style="left:348px;top:272px;width:130px;height:122px;background:var(--red);border-radius:70% 0 0 30%"></div>
  <div class="photo" style="left:478px;top:232px;width:722px;height:466px;background:linear-gradient(90deg,#f1f0ea 0%,#e8b31a 20%,#e6a80f 60%,#d99a12 100%)" role="img" aria-label="Empty room with a ladder and a wall half painted yellow"></div>
  <h3 class="service-title" style="left:48px;top:430px">Residential</h3>
  <p class="service-text" style="left:50px;top:476px">Lorem ipsum, or lipsum as it is sometimes known, is dummy text used in laying out print, graphic or web designs. The passage is attributed to an unknown typesetter in the 15th century</p>
  <a class="btn service-btn" style="left:50px;top:672px" href="#">Read More</a>

  <!-- multi family -->
  <div class="photo" style="left:0;top:784px;width:718px;height:474px;background:linear-gradient(180deg,#5d87c6 0%,#b9cbe3 40%,#e4d9c8 70%,#c9b8a0 100%)" role="img" aria-label="Painter working on the window trim of a house"></div>
  <div class="panel" style="left:718px;top:942px;width:482px;height:316px"></div>
  <div class="brush" style="left:718px;top:822px;width:110px;height:120px;background:var(--red);border-radius:0 70% 30% 0"></div>
  <h3 class="service-title" style="left:786px;top:970px">Multi Family</h3>
  <p class="service-text" style="left:784px;top:1016px">Lorem ipsum, or lipsum as it is sometimes known, is dummy text used in laying out print, graphic or web designs. The passage is attributed to an unknown typesetter in the 15th century</p>
  <a class="btn service-btn" style="left:784px;top:1206px" href="#">Read More</a>

  <!-- commercial -->
  <div class="panel" style="left:0;top:1488px;width:478px;height:362px"></div>
  <div class="brush" style="left:368px;top:1394px;width:110px;height:94px;background:var(--red);border-radius:70% 0 0 30%"></div>
  <div class="photo" style="left:478px;top:1334px;width:722px;height:476px;background:linear-gradient(90deg,#dfe6ea 0%,#9fb3c3 45%,#3f6588 75%,#29496b 100%)" role="img" aria-label="Rope access painter working on a glass office facade"></div>
  <h3 class="service-title" style="left:48px;top:1530px">Commercial</h3>
  <p class="service-text" style="left:50px;top:1576px">Lorem ipsum, or lipsum as it is sometimes known, is dummy text used in laying out print, graphic or web designs. The passage is attributed to an unknown typesetter in the 15th century</p>
  <a class="btn service-btn" style="left:50px;top:1762px" href="#">Read More</a>
</section>

<div class="phone">555-214-0388</div>

<!-- gallery -->
<h2 class="title" style="top:3040px">GALLERY</h2>
<svg class="rule" style="top:3100px" viewBox="0 0 260 20"><line x1="0" y1="9" x2="95" y2="9" stroke="#d9232e" stroke-width="2"/><line x1="165" y1="9" x2="260" y2="9" stroke="#d9232e" stroke-width="2"/><path d="M118 3h24v7h-24z M128 10h4v10h-4z" fill="none" stroke="#d9232e" stroke-width="2"/></svg>
<div class="gallery-tile" style="left:0;top:3168px;background:linear-gradient(90deg,#d9d5cd,#7a624a)" role="img" aria-label="Gym interior with a reclaimed wood feature wall"></div>
<div class="gallery-tile" style="left:403px;top:3168px;background:linear-gradient(180deg,#2a2d33,#8a8e94)" role="img" aria-label="Fitness studio with a patterned mural wall"></div>
<div class="gallery-tile" style="left:806px;top:3168px;background:linear-gradient(180deg,#eef0f0,#8a7b6a)" role="img" aria-label="White kitchen with an island and pendant lights"></div>
<div class="gallery-tile" style="left:0;top:3458px;background:linear-gradient(180deg,#d8d4cc,#4b4036)" role="img" aria-label="Kitchen with dark countertop and tiled backsplash"></div>
<div class="gallery-tile" style="left:403px;top:3458px;background:linear-gradient(180deg,#4f8ed4,#c7b9a3 60%,#6f8f4c)" role="img" aria-label="Single storey building exterior with lawn"></div>
<div class="gallery-tile" style="left:806px;top:3458px;background:linear-gradient(180deg,#5d95d3,#d6c8b2 60%,#a09a8c)" role="img" aria-label="Freshly painted building exterior with a dark roof"></div>

<!-- recent project -->
<h3 class="abs" style="left:67px;top:3822px;font-size:35px;color:var(--navy)">Our Recent Project</h3>
<p class="abs" style="left:69px;top:3920px;width:490px;font-size:20.5px;line-height:25.5px;color:#333">Lorem ipsum, or lipsum as it is sometimes known, is dummy text used in laying out print, graphic or web designs. The passage is attributed to an unknown typesetter in the 15th century</p>
<a class="btn" style="left:74px;top:4110px;width:142px;height:42px;font-size:22px" href="#">Read More</a>
<div class="photo" style="left:598px;top:3776px;width:275px;height:450px;background:linear-gradient(180deg,#f2f3f3,#c7c4be)" role="img" aria-label="Room after painting with clean white walls"></div>
<div class="photo" style="left:873px;top:3776px;width:274px;height:450px;background:linear-gradient(180deg,#cdcac4,#8f8a82)" role="img" aria-label="Room before painting with worn grey walls"></div>
<div class="abs" style="left:871px;top:3776px;width:4px;height:450px;background:var(--white)"></div>
<svg class="abs" style="left:840px;top:3968px" width="66" height="66" viewBox="0 0 66 66"><circle cx="33" cy="33" r="32" fill="#fff"/><path d="M24 33l7-6v12z M42 33l-7-6v12z" fill="#666"/></svg>

<!-- quote -->
<div class="photo" style="left:0;top:4294px;width:536px;height:560px;background:linear-gradient(135deg,#f2b325 0%,#f0c23a 45%,#7fe4c8 70%,#efeae0 100%)" role="img" aria-label="Paint cans, ladder and rollers in front of a freshly painted wall"></div>
<div class="quote-bg"></div>
<h2 class="quote-title">START WITH<br>A FREE QUOTE!</h2>
<div class="field" style="top:4495px;height:60px">Your Name</div>
<div class="field" style="top:4574px;height:60px">Your E-mail</div>
<div class="field" style="top:4650px;height:140px">Message</div>
<a class="btn" style="left:598px;top:4806px;width:142px;height:44px;font-size:22px" href="#">Send</a>

<!-- footer -->
<footer class="footer">
  <div class="footer-brand"><span class="brand-dot"></span>HARTWELL</div>
  <h3 style="left:108px;top:158px">Contact Details</h3>
  <div class="contact-row" style="left:142px;top:226px">
    <svg width="18" height="24" viewBox="0 0 18 24"><rect x="2" y="1" width="14" height="22" rx="3" fill="none" stroke="#fff" stroke-width="2"/><circle cx="9" cy="19" r="1.5" fill="#fff"/></svg>123-456-7890</div>
  <div class="contact-row" style="left:84px;top:268px">
    <svg width="24" height="24" viewBox="0 0 24 24"><circle cx="12" cy="12" r="10" fill="none" stroke="#fff" stroke-width="2"/><circle cx="12" cy="12" r="4" fill="none" stroke="#fff" stroke-width="2"/></svg>info@yoursite.com</div>
  <div class="contact-row" style="left:82px;top:310px;align-items:flex-start">
    <svg width="22" height="26" viewBox="0 0 22 26"><path d="M11 2a7 7 0 0 0-7 7c0 5 7 11 7 11s7-6 7-11a7 7 0 0 0-7-7z" fill="none" stroke="#fff" stroke-width="2"/><circle cx="11" cy="9" r="2.5" fill="#fff"/><ellipse cx="11" cy="23" rx="8" ry="2" fill="none" stroke="#fff" stroke-width="1.5"/></svg>
    <span style="text-align:right;line-height:22px">6198 Your Address<br>Street</span></div>
  <p class="footer-note">Our experienced estimators willnmeet with you and customize a proposal to meet your needs. They will stay with you from the beginning of the project to the end, making sure you are 100% satisfied.</p>
  <h3 style="left:882px;top:155px">Painting License</h3>
  <p class="license" style="top:226px">Residential / Commerical</p>
  <p class="license" style="top:258px">Painting license #1234</p>
</footer>

</body>
</html>
```